Creation of a book cover
Size : 14 x 20,5 cm (+ 5 mm bleed area at the top, bottom and right areas)
The Title is a French sentence which means “The heron dreaming on the cold roof of this empty station”. It’s a surrealistic title which has no link to the story.
AUTHOR : Mathieu Vorlange
TITLE : "Le héron rêvant sur le toit froid de cette gare vide »
PUBLISHER (AT THE BOTTOM OF THE PAGE) : Editions Parvenche
I send a PDF file with the kind of cover we have imagine, but you can propose something different. The glass and the fly can of course be used.

```html
<!DOCTYPE html>
<html lang="fr">
<head>
<meta charset="utf-8">
<title>Le héron rêvant sur le toit froid de cette gare vide — Mathieu Vorlange</title>
<link rel="stylesheet" href="https://fonts.googleapis.com/css2?family=Anton&family=Arimo:wght@400&family=Oswald:wght@600&display=swap">
<style>
  :root {
    --paper: #ffffff;
    --ink: #3a3a3a;
    --ink-soft: #4a4a4a;
    --title-red: #b3131b;
    --glass-light: #f4f5f6;
    --glass-mid: #d9dcdf;
    --glass-dark: #9ea3a8;
  }
  html, body {
    margin: 0;
    padding: 0;
    width: 820px;
    height: 1200px;
    overflow: hidden;
    background: var(--paper);
  }
  .cover {
    position: relative;
    width: 820px;
    height: 1200px;
    background: var(--paper);
  }
  .author {
    position: absolute;
    top: 28px;
    left: 0;
    width: 100%;
    margin: 0;
    text-align: center;
    font-family: "Arimo", Arial, sans-serif;
    font-weight: 400;
    font-size: 36px;
    color: var(--ink-soft);
    letter-spacing: 0.5px;
  }
  .title {
    position: absolute;
    top: 170px;
    left: 0;
    width: 100%;
    margin: 0;
    text-align: center;
    text-transform: uppercase;
  }
  .title-lead {
    display: block;
    font-family: "Anton", Impact, sans-serif;
    font-weight: 400;
    font-size: 104px;
    line-height: 1.02;
    color: var(--title-red);
    letter-spacing: 1px;
  }
  .title-rest {
    display: block;
    margin-top: 6px;
    font-family: "Oswald", "Arial Narrow", sans-serif;
    font-weight: 600;
    font-size: 58px;
    line-height: 1.08;
    color: var(--ink);
    letter-spacing: 0.5px;
  }
  .glass-photo {
    position: absolute;
    top: 600px;
    left: 260px;
    width: 300px;
    height: 450px;
  }
  .publisher {
    position: absolute;
    right: 88px;
    bottom: 62px;
    margin: 0;
    font-family: "Arimo", Arial, sans-serif;
    font-size: 25px;
    color: var(--ink-soft);
  }
</style>
</head>
<body>
  <main class="cover">
    <p class="author">Mathieu Vorlange</p>
    <h1 class="title">
      <span class="title-lead">Le héron</span>
      <span class="title-rest">rêvant sur le toit froid<br>de cette gare vide</span>
    </h1>
    <svg class="glass-photo" viewBox="0 0 300 450" role="img" aria-label="Photographie d’un verre d’eau posé sur une surface blanche avec son reflet, un insecte flottant à la surface">
      <defs>
        <linearGradient id="glassTone" x1="0" y1="0" x2="1" y2="0">
          <stop offset="0" stop-color="var(--glass-mid)"/>
          <stop offset="0.5" stop-color="var(--glass-light)"/>
          <stop offset="1" stop-color="var(--glass-dark)"/>
        </linearGradient>
        <linearGradient id="reflectionFade" x1="0" y1="0" x2="0" y2="1">
          <stop offset="0" stop-color="var(--glass-mid)" stop-opacity="0.6"/>
          <stop offset="1" stop-color="var(--glass-light)" stop-opacity="0"/>
        </linearGradient>
      </defs>
      <rect x="20" y="0" width="260" height="300" rx="6" fill="url(#glassTone)"/>
      <rect x="20" y="305" width="260" height="145" rx="6" fill="url(#reflectionFade)"/>
    </svg>
    <p class="publisher">Éditions Parvenche</p>
  </main>
</body>
</html>
```